Membership card design for video game arena

I need a two sided design for membership cards for my customers. It needs to have instructions on how to book on one side, and a nice catchy design for the other.

Please pull logo and whatever you desire from the website www.vornik-play.com

Industry/Entity Type

Entertainment

Contact Information for Business Card

The front must say Vornik-Play with the address and whatever design you choose. The back must have the details below

Colors

Designer to choose colors to be used in the design.

Requirements
Must have
• Frontside
• Company name address and phone number
• Backside
• Booking Instructions
• www.Vornik-Play.com/book-now
• Click on General Admission and input information
• Use code Gatepass7 to gain access
• See you there!
Nice to have
• A nice design and whatever you find is pertinent
Should not have
• Useless info

```html
<!DOCTYPE html>
<html lang="en">
<head>
<meta charset="utf-8">
<title>Vornik-Play Membership Card</title>
<link rel="stylesheet" href="https://fonts.googleapis.com/css2?family=Exo+2:wght@300;500;700;800&display=swap">
<style>
  :root {
    --page-bg: #e4e6ea;
    --ink-white: #ffffff;
    --ink-soft: #f1e9ff;
    --violet-deep: #2a1248;
    --violet-mid: #4a2a8a;
    --indigo: #3b3fb0;
    --magenta: #d04ec9;
    --pink-glow: #f28bd6;
    --blue-glow: #7a86ff;
    --haze: #8a5a86;
    --frame-red: #7a1e2a;
    --photo-blue: #2b4fb8;
    --photo-deep: #1a2470;
  }
  * { box-sizing: border-box; margin: 0; padding: 0; }
  html, body {
    width: 1200px; height: 800px; overflow: hidden;
    background: var(--page-bg);
    font-family: "Exo 2", sans-serif;
    color: var(--ink-white);
  }
  .sheet {
    position: relative; width: 1200px; height: 800px;
  }
  .card {
    position: absolute; left: 310px;
    width: 580px; height: 332px;
    border-radius: 22px; overflow: hidden;
    box-shadow: 0 6px 18px rgba(30, 20, 60, 0.25);
  }
  .card--back { top: 46px; }
  .card--front { top: 422px; }

  /* Back side */
  .back-field {
    position: absolute; inset: 0;
    background: radial-gradient(ellipse at 50% 50%, var(--violet-mid) 0%, var(--violet-deep) 75%);
  }
  .booking-panel {
    position: absolute; left: 80px; top: 52px; width: 420px; height: 178px;
    border-radius: 20px;
    background: linear-gradient(180deg, var(--magenta) 0%, var(--pink-glow) 35%, var(--blue-glow) 75%, var(--indigo) 100%);
    box-shadow: 0 0 30px rgba(210, 110, 230, 0.55);
    text-align: center; padding-top: 20px;
  }
  .booking-title { font-size: 22px; font-weight: 700; letter-spacing: 0.5px; }
  .booking-url { font-size: 16px; font-weight: 700; margin-top: 8px; }
  .booking-step { font-size: 15px; font-weight: 300; margin-top: 8px; }
  .booking-step strong { font-weight: 700; }
  .sign-off {
    position: absolute; left: 0; right: 0; top: 254px;
    text-align: center; font-size: 22px; font-weight: 800;
  }

  /* Front side */
  .front-photo {
    position: absolute; inset: 0;
    background: linear-gradient(160deg, #3a2a78 0%, #5a3a86 40%, var(--haze) 70%, #3a2240 100%);
  }
  .brand {
    position: absolute; left: 26px; top: 22px;
    display: flex; align-items: center; gap: 12px;
  }
  .brand-dot {
    width: 30px; height: 30px; border-radius: 50%; background: var(--ink-white);
  }
  .brand-name { font-size: 36px; font-weight: 800; letter-spacing: 1px; line-height: 1; }
  .brand-tagline {
    position: absolute; left: 80px; top: 66px;
    font-size: 18px; font-weight: 300; letter-spacing: 1.5px; color: var(--ink-soft);
  }
  .member-band {
    position: absolute; left: 0; top: 132px; width: 360px; height: 78px;
    background: rgba(255, 255, 255, 0.22);
    padding: 12px 0 0 34px;
  }
  .member-name { font-size: 22px; font-weight: 800; line-height: 1.2; letter-spacing: 0.5px; }
  .action-photos { position: absolute; right: 16px; top: 110px; }
  .address {
    position: absolute; left: 40px; top: 278px;
    font-size: 17px; font-weight: 500; letter-spacing: 0.5px;
  }
</style>
</head>
<body>
<main class="sheet">

  <section class="card card--back" aria-label="Membership card, booking side">
    <div class="back-field" role="img" aria-label="Glowing purple circuit-board backdrop"></div>
    <div class="booking-panel">
      <h2 class="booking-title">Booking Instructions</h2>
      <p class="booking-url">www.Vornik-Play.com/book-now</p>
      <p class="booking-step">Click on <strong>General Admission</strong> &amp; input information</p>
      <p class="booking-step">Use code <strong>Gatepass7</strong> to gain access</p>
    </div>
    <p class="sign-off">See you there!</p>
  </section>

  <section class="card card--front" aria-label="Membership card, member side">
    <div class="front-photo" role="img" aria-label="Virtual reality arena with a motion rig in hazy violet light"></div>
    <div class="brand">
      <span class="brand-dot"></span>
      <span class="brand-name">VORNIK-PLAY</span>
    </div>
    <p class="brand-tagline">MEMBERSHIP CARDS</p>
    <div class="member-band">
      <p class="member-name">MEMBERNAME</p>
      <p class="member-name">LASTNAME</p>
    </div>
    <svg class="action-photos" width="250" height="160" viewBox="0 0 250 160">
      <defs>
        <linearGradient id="photoTone" x1="0" y1="0" x2="0" y2="1">
          <stop offset="0" stop-color="var(--photo-blue)"/>
          <stop offset="1" stop-color="var(--photo-deep)"/>
        </linearGradient>
      </defs>
      <g role="img" aria-label="Player in VR headset and haptic vest">
        <polygon points="10,70 50,38 110,42 130,92 90,150 30,146" fill="url(#photoTone)" stroke="var(--frame-red)" stroke-width="4"/>
      </g>
      <g role="img" aria-label="Player aiming a VR blaster on a motion platform">
        <polygon points="112,30 172,4 232,30 240,86 180,124 128,96" fill="url(#photoTone)" stroke="var(--frame-red)" stroke-width="4"/>
      </g>
    </svg>
    <p class="address">2715 W Calder Ave, Tampa FL 33607</p>
  </section>

</main>
</body>
</html>
```